'SOLVANO' NEW WINE LABEL DESIGN

I am looking for an exceptional and exciting design for a wine label called 'Solvano' meaning 'Lookout'. The design must feature the name 'Solvano', and the word 'Cabernet Sauvignon' in version 1 and 'Sauvignon Blanc' in version 2. It will also need the words 'Valle Central, Chile' at the bottom of the label as a prominent piece of information as well as the vintage 2017. Please produce the work in size 80mm x 100mm. Feel free to use colour in addition to black/white and ensue that the label is easy to read on a shelf placement.
Low design quality
Target Market(s)
SUPERMARKETS & WINE STORES
Requirements
Must have
- EASY TO READ, USE COLOURS LIKE GREEN FOR SAUVIGNON & RED FOR CABERNET SAUVIGNON
- FULL BOTTLE SHOT MUST BE IN PROVIDED DESIGNS. ALL BOTTLE TOPS SHOULD BE VENDRAX STYLE (SCREW TOP)
- PLEASE NOTE THAT LABEL INFORMATION MUSY BE EASY TO READ I.E. VINTAGE, PLACE OF ORGIN ALTHOUGH NOT THE MAIN CONTENT MUST STILL BE CLEAR.
Nice to have
- ARTISTIC REFERENCE LINK TO NAME & ANDES BUT NOT PICTURES OF MOUNTAINS
Should not have
- PICTURES OF GRAPES
- PICTURES OF VINEYARDS
- PICTURES OF MOUNTAINS

```html
<!DOCTYPE html>
<html lang="en">
<head>
<meta charset="utf-8">
<title>Solvano – Cabernet Sauvignon Label</title>
<link rel="stylesheet" href="https://fonts.googleapis.com/css2?family=Cinzel:wght@700&family=Montserrat:wght@500;600&family=Libre+Baskerville&display=swap">
<style>
  :root {
    --backdrop: #dcdcdc;
    --label-black: #0c0b0b;
    --label-edge: #1d1c1c;
    --gold: #d89b1c;
    --gold-light: #f3c23a;
    --gold-deep: #9c6410;
    --ink-brown: #3e2705;
  }
  * { margin: 0; padding: 0; box-sizing: border-box; }
  html, body {
    width: 1124px;
    height: 1200px;
    overflow: hidden;
    background: var(--backdrop);
  }
  .canvas {
    position: relative;
    width: 1124px;
    height: 1200px;
  }

  /* Capsule wrap (screw top) */
  .capsule {
    position: absolute;
    left: 120px;
    top: 560px;
    width: 190px;
    height: 340px;
    background: linear-gradient(90deg, var(--label-edge), var(--label-black) 40%, var(--label-edge));
    border-radius: 8px;
    display: flex;
    flex-direction: column;
    align-items: center;
  }
  .capsule-ridges {
    width: 100%;
    margin-top: 70px;
    height: 22px;
    background: repeating-linear-gradient(90deg, #2a2929 0 3px, var(--label-black) 3px 7px);
  }
  .capsule-emblem {
    margin-top: 60px;
    width: 120px;
    height: 82px;
    border-radius: 6px;
    background: linear-gradient(135deg, var(--gold-light), var(--gold-deep));
  }
  .capsule-name {
    margin-top: 16px;
    font-family: "Montserrat", sans-serif;
    font-weight: 600;
    font-size: 27px;
    letter-spacing: 0.5px;
    color: var(--gold);
  }

  /* Front label 80 x 100 mm */
  .label {
    position: absolute;
    left: 440px;
    top: 220px;
    width: 560px;
    height: 700px;
    background: radial-gradient(ellipse at 50% 45%, #1a1919, var(--label-black) 70%);
    border-radius: 6px;
    text-align: center;
  }
  .varietal-band {
    position: absolute;
    left: 130px;
    top: 200px;
    width: 300px;
    height: 46px;
    border-radius: 4px;
    background: linear-gradient(90deg, #a8690f, var(--gold-light) 50%, #a8690f);
    display: flex;
    align-items: center;
    justify-content: center;
  }
  .varietal-text {
    font-family: "Libre Baskerville", serif;
    font-size: 16px;
    letter-spacing: 0.5px;
    color: var(--ink-brown);
  }
  .varietal-number {
    position: absolute;
    left: 0;
    right: 0;
    top: 248px;
    font-family: "Libre Baskerville", serif;
    font-size: 40px;
    line-height: 1;
    color: var(--gold-deep);
  }
  .owl-emblem {
    position: absolute;
    left: 318px;
    top: 276px;
    width: 90px;
    height: 62px;
    border-radius: 6px;
    background: linear-gradient(135deg, var(--gold-light), var(--gold-deep));
  }
  .wine-name {
    position: absolute;
    left: 0;
    right: 0;
    top: 352px;
    font-family: "Cinzel", serif;
    font-weight: 700;
    font-size: 64px;
    line-height: 1.2;
    letter-spacing: 2px;
    color: var(--gold);
  }
  .vintage {
    position: absolute;
    left: 0;
    right: 0;
    top: 458px;
    font-family: "Montserrat", sans-serif;
    font-weight: 500;
    font-size: 24px;
    letter-spacing: 1px;
    color: var(--gold);
  }
  .origin {
    position: absolute;
    left: 0;
    right: 0;
    top: 540px;
    font-family: "Montserrat", sans-serif;
    font-weight: 500;
    font-size: 15px;
    color: var(--gold);
  }
</style>
</head>
<body>
<main class="canvas">

  <section class="capsule" aria-label="Screw cap capsule">
    <div class="capsule-ridges"></div>
    <div class="capsule-emblem" role="img" aria-label="Golden owl in flight illustration"></div>
    <p class="capsule-name">SOLVANO</p>
  </section>

  <section class="label" aria-label="Front label">
    <div class="varietal-band" role="img" aria-label="Curved gold ribbon ornament">
      <span class="varietal-text">CABERNET SAUVIGNON</span>
    </div>
    <p class="varietal-number">1</p>
    <div class="owl-emblem" role="img" aria-label="Golden owl in flight illustration"></div>
    <h1 class="wine-name">SOLVANO</h1>
    <p class="vintage">VINTAGE 2017</p>
    <p class="origin">Valle Central, Chile</p>
  </section>

</main>
</body>
</html>
```